Investment Advisor Firm Needs a Web Site Design

Brenwick Capital Web Design
We are looking a website design for an Investment Advisor firm in Latin America. Our target is high net clients that are looking for investment solutions such as portfolios and investment opportunities. Colors like gold and black would be preferred. Client will be looking information in our website such as:
• Market Data
• Market Articles
• Market research
• Main commodity products index price
• Indexes and pricing at market
• Audio interviews of top financial speakers in the market
• Educational material
• Investment Objectives
• Latin America top financial news

```html
<!DOCTYPE html>
<html lang="en">
<head>
<meta charset="utf-8">
<title>Brenwick Capital</title>
<link rel="stylesheet" href="https://fonts.googleapis.com/css2?family=Open+Sans:wght@400;600;700&family=Raleway:wght@400;500;600&display=swap">
<style>
:root{
  --black:#141414;
  --charcoal:#222222;
  --gold:#c9951c;
  --gold-light:#e0b54a;
  --gold-dark:#a67812;
  --white:#ffffff;
  --paper:#f4f4f4;
  --band:#e4e4e4;
  --text:#333333;
  --muted:#777777;
  --footer-text:#b5b5b5;
}
*{box-sizing:border-box;margin:0;padding:0}
html,body{width:784px;height:1200px;overflow:hidden}
body{position:relative;background:var(--white);font-family:"Open Sans",Arial,sans-serif;color:var(--text)}
.abs{position:absolute}

/* header */
.site-header{left:0;top:0;width:784px;height:47px;background:var(--black)}
.brand{left:123px;top:12px;display:flex;align-items:center;gap:7px;color:var(--white);font-size:11px;font-weight:700;letter-spacing:1px;text-transform:uppercase}
.brand-mark{width:14px;height:14px;background:var(--gold)}
.main-nav{right:118px;top:18px;display:flex;gap:20px}
.main-nav a{color:var(--white);font-size:9px;text-decoration:none}

/* hero */
.hero{left:0;top:47px;width:784px;height:339px;background:linear-gradient(180deg,#d9a648 0%,#a47a45 35%,#5b5149 70%,#3f3c3a 100%)}
.hero-panel{left:144px;top:144px;width:274px;height:130px;background:rgba(201,149,28,.88);padding:16px 20px}
.hero-title{font-family:"Raleway",sans-serif;font-size:24px;line-height:30px;font-weight:500;color:var(--white)}
.hero-text{margin-top:8px;font-size:8px;line-height:12px;color:var(--white);width:220px}
.hero-dots{left:372px;top:370px;display:flex;gap:5px}
.hero-dots span{width:7px;height:7px;border-radius:50%;background:rgba(255,255,255,.55)}
.hero-dots span.active{background:var(--white)}

/* feature cards */
.feature-band{left:0;top:386px;width:784px;height:170px;background:var(--paper)}
.feature-card{top:410px;width:170px;height:130px;box-shadow:0 2px 5px rgba(0,0,0,.2)}
.feature-photo{width:100%;height:100%}
.feature-label{position:absolute;left:0;bottom:0;width:100%;height:30px;background:rgba(201,149,28,.9);color:var(--white);font-family:"Raleway",sans-serif;font-size:13px;font-weight:500;text-align:center;line-height:30px}

/* commodity products */
.products{left:0;top:556px;width:784px;height:227px;background:var(--band)}
.section-title{font-family:"Raleway",sans-serif;font-size:15px;font-weight:500;color:var(--text)}
.products-title{left:0;top:585px;width:784px;text-align:center}
.product-card{top:616px;width:116px;height:141px;background:var(--white);box-shadow:0 2px 4px rgba(0,0,0,.15)}
.product-photo{width:116px;height:72px}
.product-name{padding:7px 8px 2px;font-size:8px;font-weight:700;color:var(--gold)}
.product-text{padding:0 8px;font-size:6.5px;line-height:9px;color:var(--muted)}
.slider-arrow{top:672px;width:12px;height:24px}

/* media & indexes */
.media-title{color:var(--gold);font-size:14px;line-height:17px}
.audio-title{left:123px;top:812px;width:260px}
.index-title{left:412px;top:812px;width:250px}
.audio-photo{top:852px;width:82px;height:50px}
.audio-text{left:123px;top:912px;width:262px;font-size:7px;line-height:10px;color:var(--muted)}
.index-item{top:852px;width:118px}
.index-photo{width:118px;height:50px}
.index-item h4{margin-top:6px;font-size:7.5px;font-weight:700;color:var(--text)}
.index-item p{margin-top:2px;font-size:6.5px;line-height:9px;color:var(--muted)}

/* footer */
.site-footer{left:0;top:1018px;width:784px;height:182px;background:var(--charcoal)}
.footer-col{top:1038px;width:120px}
.footer-col h5{font-size:9px;font-weight:700;color:var(--white);margin-bottom:6px}
.footer-col li{list-style:none;font-size:7px;line-height:11px;color:var(--footer-text)}
.footer-col p{font-size:7px;line-height:11px;color:var(--footer-text)}
.social{display:flex;gap:4px;margin-top:6px}
.social span{width:14px;height:14px;background:var(--footer-text)}
.footer-rule{left:123px;top:1160px;width:537px;height:1px;background:#3a3a3a}
.copyright{left:123px;top:1168px;font-size:6.5px;color:#8a8a8a}
</style>
</head>
<body>

<header class="abs site-header">
  <div class="abs brand"><span class="brand-mark"></span>Brenwick Capital</div>
  <nav class="abs main-nav">
    <a href="#">About Us</a><a href="#">Services</a><a href="#">Projects</a><a href="#">Consulting</a><a href="#">Research</a><a href="#">Contact</a>
  </nav>
</header>

<section class="abs hero" role="img" aria-label="City skyline of office towers at sunset"></section>
<div class="abs hero-panel">
  <h1 class="hero-title">Market Research &amp;<br>Financial Services</h1>
  <p class="hero-text">Independent advice for private clients across Latin America since 1998.</p>
</div>
<div class="abs hero-dots"><span class="active"></span><span></span><span></span><span></span><span></span></div>

<section class="abs feature-band"></section>
<article class="abs feature-card" style="left:123px">
  <div class="feature-photo" role="img" aria-label="Stock market data board" style="background:linear-gradient(160deg,#3a6f9c,#1d3b5a)"></div>
  <div class="feature-label">Market Data</div>
</article>
<article class="abs feature-card" style="left:306px">
  <div class="feature-photo" role="img" aria-label="Business people reading market articles" style="background:linear-gradient(160deg,#dfe3e8,#7f8a96)"></div>
  <div class="feature-label">Market Articles</div>
</article>
<article class="abs feature-card" style="left:490px">
  <div class="feature-photo" role="img" aria-label="Research charts and documents" style="background:linear-gradient(160deg,#cfd6dc,#8c979f)"></div>
  <div class="feature-label">Market Research</div>
</article>

<section class="abs products"></section>
<h2 class="abs section-title products-title">Main Commodity Products</h2>
<svg class="abs slider-arrow" style="left:94px" viewBox="0 0 12 24"><path d="M10 2 L2 12 L10 22" fill="none" stroke="#888" stroke-width="2"/></svg>
<svg class="abs slider-arrow" style="left:678px" viewBox="0 0 12 24"><path d="M2 2 L10 12 L2 22" fill="none" stroke="#888" stroke-width="2"/></svg>

<article class="abs product-card" style="left:157px">
  <div class="product-photo" role="img" aria-label="Price chart on a trading screen" style="background:linear-gradient(160deg,#2d6fb0,#0f2a4c)"></div>
  <h3 class="product-name">Product Name</h3>
  <p class="product-text">Spot price, daily change and volume for this index.</p>
</article>
<article class="abs product-card" style="left:283px">
  <div class="product-photo" role="img" aria-label="Stock ticker board" style="background:linear-gradient(160deg,#3d3d3d,#8a8a8a)"></div>
  <h3 class="product-name">Product Name</h3>
  <p class="product-text">Spot price, daily change and volume for this index.</p>
</article>
<article class="abs product-card" style="left:410px">
  <div class="product-photo" role="img" aria-label="Financial report with magnifier" style="background:linear-gradient(160deg,#e6e9ec,#9aa4ad)"></div>
  <h3 class="product-name">Product Name</h3>
  <p class="product-text">Spot price, daily change and volume for this index.</p>
</article>
<article class="abs product-card" style="left:537px">
  <div class="product-photo" role="img" aria-label="Market line chart on screen" style="background:linear-gradient(160deg,#1f5fa8,#0b1f3d)"></div>
  <h3 class="product-name">Product Name</h3>
  <p class="product-text">Spot price, daily change and volume for this index.</p>
</article>

<h2 class="abs section-title media-title audio-title">Audio interviews of top financial<br>Speakers in the market</h2>
<div class="abs audio-photo" style="left:123px" role="img" aria-label="Speaker at an interview" style="background:#9aa7b2"></div>
<div class="abs audio-photo" style="left:123px;background:linear-gradient(160deg,#b7c1ca,#6e7c88)" role="img" aria-label="Speaker at an interview"></div>
<div class="abs audio-photo" style="left:213px;background:linear-gradient(160deg,#c9ced3,#7b8690)" role="img" aria-label="Panel of financial speakers"></div>
<div class="abs audio-photo" style="left:303px;background:linear-gradient(160deg,#a9b3bc,#5f6b76)" role="img" aria-label="Recording microphone and headphones"></div>
<p class="abs audio-text">Listen to fund managers, economists and strategists discuss rates, currencies and regional equity markets in weekly recorded sessions for our clients.</p>

<h2 class="abs section-title media-title index-title">Indexes and pricing at market</h2>
<article class="abs index-item" style="left:412px">
  <div class="index-photo" role="img" aria-label="Index price board" style="background:linear-gradient(160deg,#2b5f93,#0e2540)"></div>
  <h4>Latest index report</h4>
  <p>Closing levels and weekly moves for regional benchmark indexes.</p>
</article>
<article class="abs index-item" style="left:542px">
  <div class="index-photo" role="img" aria-label="Pricing chart on a monitor" style="background:linear-gradient(160deg,#2a8ad0,#123b66)"></div>
  <h4>Latest index report</h4>
  <p>Closing levels and weekly moves for regional benchmark indexes.</p>
</article>

<footer class="abs site-footer"></footer>
<div class="abs footer-col" style="left:123px">
  <h5>Company</h5>
  <ul><li>About Us</li><li>Our Team</li><li>Careers</li><li>Contact</li></ul>
</div>
<div class="abs footer-col" style="left:263px">
  <h5>Our Services</h5>
  <ul><li>Portfolios</li><li>Advisory</li><li>Wealth Planning</li><li>Education</li></ul>
</div>
<div class="abs footer-col" style="left:403px">
  <h5>Resources</h5>
  <ul><li>Support</li><li>FAQ</li><li>Market News</li><li>Glossary</li></ul>
</div>
<div class="abs footer-col" style="left:543px">
  <h5>Get in Touch</h5>
  <p>Speak with an advisor today.</p>
  <div class="social"><span></span><span></span><span></span></div>
</div>
<div class="abs footer-rule"></div>
<p class="abs copyright">© 2024 Brenwick Capital. All rights reserved.</p>

</body>
</html>
```